Business card for real estate agent / office

We're looking for a new business card. We want something that is pretty clean, modern and sleek. Something that also tells people that we are a new age company...cutting edge. Although real estate has been done a certain way the last 100 years, we have energy and vibrance. Company name is Silver Meadow Properties. info can be found here: http://www.smprealtyhub.example/

needs to include: Name, title, phone number, email. our license number also needs to be displayed somewhere.

Target Market(s)

25-55 homeowners or potential homeowners

Industry/Entity Type

Business

Contact Information for Business Card

we need business card designs for real estate agent / office

Font styles to use
Serif

Requirements
Must have
• needs to include: Name, title, phone number, email. our license number also needs to be displayed somewhere and company name.
Nice to have
• placement area for photo

```html
<!DOCTYPE html>
<html lang="en">
<head>
<meta charset="utf-8">
<title>Silver Meadow Properties – Business Card</title>
<link rel="stylesheet" href="https://fonts.googleapis.com/css2?family=Quicksand:wght@500;600&family=Merriweather:wght@700&display=swap">
<style>
  :root {
    --backdrop: #87720e;
    --card: #ffffff;
    --navy: #1a4a72;
    --green: #5db848;
    --photo-dark: #2b2b2b;
    --photo-light: #9a9a9a;
  }
  * { margin: 0; padding: 0; box-sizing: border-box; }
  html, body { width: 1200px; height: 1200px; overflow: hidden; }
  body {
    background: var(--backdrop);
    position: relative;
    font-family: "Quicksand", sans-serif;
    color: var(--navy);
  }
  .card {
    position: absolute;
    width: 840px;
    height: 480px;
    background: var(--card);
  }
  .card--front { left: 54px; top: 105px; }
  .card--back { left: 273px; top: 644px; }

  .outline-square {
    position: absolute;
    border: 3px solid var(--navy);
  }
  .outline-square--green { border-color: var(--green); }

  .photo-frame-back { left: 56px; top: 45px; width: 134px; height: 134px; }
  .photo {
    position: absolute;
    left: 72px; top: 58px; width: 134px; height: 134px;
    border: 3px solid var(--green);
    background: radial-gradient(circle at 50% 40%, var(--photo-light), var(--photo-dark) 75%);
  }

  .agent-name {
    position: absolute; left: 239px; top: 114px;
    font-size: 21px; font-weight: 600; white-space: nowrap;
  }
  .agent-name .surname { color: var(--green); }
  .agent-title {
    position: absolute; left: 238px; top: 153px;
    font-size: 14px; font-weight: 500; color: var(--green);
  }

  .contact-list { position: absolute; left: 72px; top: 303px; list-style: none; }
  .contact-item {
    display: flex; align-items: center; height: 24px; margin-bottom: 23px;
    font-size: 14.5px; font-weight: 500;
  }
  .contact-badge {
    width: 24px; height: 24px; border-radius: 50%;
    background: var(--green); color: #fff;
    font-family: "Merriweather", serif; font-size: 10px;
    display: flex; align-items: center; justify-content: center;
    margin-right: 23px;
  }

  .divider { position: absolute; left: 437px; top: 157px; width: 16px; height: 280px; }

  .brand {
    position: absolute;
    text-align: center;
    font-weight: 600;
    color: var(--navy);
    line-height: 1.1;
  }
  .brand-square {
    display: block; margin: 0 auto 10px;
    width: 22px; height: 22px; background: var(--green);
  }
  .brand--front { left: 556px; top: 78px; width: 240px; font-size: 24px; }
  .brand--back { left: 273px; top: 190px; width: 280px; font-size: 28px; }
  .brand--back .brand-square { width: 28px; height: 28px; }

  .office-address {
    position: absolute; left: 597px; top: 382px;
    font-size: 13.5px; font-weight: 500; line-height: 20px;
  }

  .license-number {
    position: absolute; right: 21px; top: 15px;
    font-family: "Merriweather", serif; font-size: 12px; font-weight: 700;
  }
  .corner-navy-top { left: 49px; top: 36px; width: 56px; height: 56px; }
  .corner-green-top { left: 73px; top: 60px; width: 56px; height: 56px; }
  .corner-navy-bottom { left: 719px; top: 377px; width: 56px; height: 56px; }
  .corner-green-bottom { left: 743px; top: 401px; width: 56px; height: 56px; }
</style>
</head>
<body>

<section class="card card--front">
  <div class="outline-square photo-frame-back"></div>
  <div class="photo" role="img" aria-label="Portrait photo of the agent"></div>

  <h1 class="agent-name">Marlena <span class="surname">Voss</span></h1>
  <p class="agent-title">CEO</p>

  <ul class="contact-list">
    <li class="contact-item"><span class="contact-badge">T</span>555-310-4827</li>
    <li class="contact-item"><span class="contact-badge">E</span>info@smprealtyhub.example</li>
    <li class="contact-item"><span class="contact-badge">w</span>www.smprealtyhub.example</li>
  </ul>

  <svg class="divider" viewBox="0 0 16 280" aria-hidden="true">
    <rect x="0" y="0" width="16" height="16" fill="#1a4a72"/>
    <line x1="8" y1="16" x2="8" y2="264" stroke="#1a4a72" stroke-width="1"/>
    <rect x="0" y="264" width="16" height="16" fill="#1a4a72"/>
  </svg>

  <div class="brand brand--front"><span class="brand-square"></span>Silver Meadow<br>Properties</div>

  <p class="office-address">218 W. Harbor Lane, Suite 904<br>Bayview, Texas 70000</p>
</section>

<section class="card card--back">
  <p class="license-number">PE781302</p>
  <div class="outline-square corner-navy-top"></div>
  <div class="outline-square outline-square--green corner-green-top"></div>

  <div class="brand brand--back"><span class="brand-square"></span>Silver Meadow<br>Properties</div>

  <div class="outline-square corner-navy-bottom"></div>
  <div class="outline-square outline-square--green corner-green-bottom"></div>
</section>

</body>
</html>
```